Sheriff Candidate needs a large yard sign

A candidate for Sheriff needs to have a sign to put in front of businesses and houses that advertise her candidacy.

Target Market(s)

Democrats, voters

Industry/Entity Type

Political

Font styles to use
Sans Serif

Colors
34a7d7
3276b5

Requirements
Must have
• Must have her picture
• Must have the words "Elect Dana Whitlock" - I'd like the name Dana to be smaller Whitlock. "Elect" and "Whitlock" should be the focus.
• at the bottom in a box "Paid for by the Committee to Elect Dana Whitlock"
Nice to have
• it would be good to have her logo as well.
• blue color for democrats and on a white background
Should not have
• pink color

```html
<!DOCTYPE html>
<html lang="en">
<head>
<meta charset="utf-8">
<title>Elect Dana Whitlock – Yard Sign</title>
<link rel="stylesheet" href="https://fonts.googleapis.com/css2?family=Archivo+Black&family=Montserrat:wght@500;700&display=swap">
<style>
  :root {
    --backdrop: #e9ecef;
    --sign-white: #ffffff;
    --sky-blue: #34a7d7;
    --elect-blue: #1a7bd0;
    --navy: #1f3a9e;
    --ray-blue: #d8ecfa;
    --photo-top: #c9c3bd;
    --photo-mid: #7d6a60;
    --photo-suit: #2a2d36;
    --seal-gold: #c9a441;
  }
  html, body {
    margin: 0;
    padding: 0;
    width: 1200px;
    height: 799px;
    overflow: hidden;
    background: var(--backdrop);
  }
  .yard-sign {
    position: absolute;
    left: 40px;
    top: 49px;
    width: 1120px;
    height: 700px;
    display: block;
    box-shadow: 0 6px 24px rgba(0,0,0,0.18);
  }
  .headline-elect {
    font-family: "Archivo Black", "Arial Black", sans-serif;
    fill: var(--elect-blue);
  }
  .headline-first {
    font-family: "Archivo Black", "Arial Black", sans-serif;
    fill: var(--navy);
  }
  .headline-last {
    font-family: "Archivo Black", "Arial Black", sans-serif;
    fill: var(--navy);
  }
  .seal-name {
    font-family: "Montserrat", sans-serif;
    font-weight: 700;
    fill: var(--navy);
  }
  .disclaimer {
    font-family: "Montserrat", sans-serif;
    font-weight: 500;
    fill: var(--navy);
  }
</style>
</head>
<body>
  <svg class="yard-sign" viewBox="0 0 600 375" xmlns="http://www.w3.org/2000/svg">
    <defs>
      <radialGradient id="sign-glow" cx="0.5" cy="0.48" r="0.6">
        <stop offset="0" stop-color="#ffffff"/>
        <stop offset="0.55" stop-color="#eef6fd"/>
        <stop offset="1" stop-color="var(--ray-blue)"/>
      </radialGradient>
      <linearGradient id="portrait-fill" x1="0" y1="0" x2="0" y2="1">
        <stop offset="0" stop-color="var(--photo-top)"/>
        <stop offset="0.45" stop-color="var(--photo-mid)"/>
        <stop offset="0.8" stop-color="var(--photo-suit)"/>
        <stop offset="1" stop-color="var(--photo-suit)" stop-opacity="0"/>
      </linearGradient>
    </defs>

    <rect class="sign-face" x="0" y="0" width="600" height="375" fill="url(#sign-glow)"/>

    <rect class="candidate-portrait" x="400" y="8" width="200" height="240" fill="url(#portrait-fill)" role="img" aria-label="Portrait photo of candidate Dana Whitlock"/>

    <text class="headline-elect" x="20" y="92" font-size="96" textLength="380" lengthAdjust="spacingAndGlyphs">ELECT</text>

    <text class="headline-first" x="22" y="228" font-size="92" textLength="218" lengthAdjust="spacingAndGlyphs">Dana</text>

    <g class="campaign-seal">
      <circle cx="300" cy="172" r="30" fill="var(--seal-gold)"/>
      <text class="seal-name" x="300" y="220" font-size="10" text-anchor="middle">Whitlock for Sheriff</text>
    </g>

    <text class="headline-last" x="18" y="354" font-size="128" textLength="570" lengthAdjust="spacingAndGlyphs">WHITLOCK</text>

    <text class="disclaimer" x="300" y="368" font-size="11" text-anchor="middle">Paid for by the Committee to Elect Dana Whitlock</text>
  </svg>
</body>
</html>
```